Save the Date card

This will be a Save the Date 5x7 card...preferably Hunter Green background

Annual Fund Leadership Dinner
June 20, 2023. 6:30 pm
Location: The Pellimore's Home
4187 Brindlecove Ridge Rd
Harrison, TN 37598

Other side of card:
We would prayerfully ask that you consider partnering with us as we kick off our Annual Fund this Fall to celebrate our 25 year anniversary as an Academy.
Please direct any questions to Marla Quenby, our Director of Advancement 423-555-0184 x 3617 or advancement@corvellanprep.org

```html
<!DOCTYPE html>
<html lang="en">
<head>
<meta charset="UTF-8">
<title>Annual Fund Leadership Dinner – Save the Date</title>
<link rel="stylesheet" href="https://fonts.googleapis.com/css2?family=EB+Garamond:wght@400;500&family=Josefin+Sans:wght@400;600&display=swap">
<style>
  :root {
    --page: #ffffff;
    --hunter: #1c3522;
    --hunter-deep: #182e1e;
    --hunter-soft: #263f2b;
    --gold: #a99a5c;
    --gold-line: #b3a062;
    --ivory: #ffffff;
  }
  * { box-sizing: border-box; margin: 0; padding: 0; }
  html, body {
    width: 1200px; height: 852px; overflow: hidden;
    background: var(--page);
  }
  .canvas { position: relative; width: 1200px; height: 852px; }

  .card {
    position: absolute; top: 58px; width: 529px; height: 740px;
    overflow: hidden;
    background: linear-gradient(170deg, var(--hunter) 0%, var(--hunter) 60%, var(--hunter-deep) 100%);
    color: var(--ivory);
    font-family: "EB Garamond", Georgia, serif;
  }
  .card--front { left: 61px; }
  .card--back { left: 615px; }

  /* Front */
  .watermark {
    position: absolute; top: -8px; right: -6px;
    font-size: 84px; line-height: 70px; text-align: right;
    color: var(--hunter-soft); letter-spacing: -1px;
    text-transform: uppercase;
  }
  .title-rule {
    position: absolute; left: 42px; top: 214px;
    width: 65px; height: 2px; background: var(--gold-line);
  }
  .title {
    position: absolute; left: 42px; top: 240px;
    font-weight: 400; font-size: 51px; line-height: 57px;
  }
  .when {
    position: absolute; left: 20px; top: 563px; width: 97px;
    text-align: right; font-size: 28px; line-height: 29px;
  }
  .when__time {
    display: block; margin-top: 10px;
    font-size: 20px; color: var(--gold);
  }
  .divider {
    position: absolute; left: 149px; top: 566px;
    width: 2px; height: 116px; background: var(--gold-line);
  }
  .where { position: absolute; left: 174px; top: 589px; }
  .where__label {
    font-family: "Josefin Sans", Arial, sans-serif;
    font-size: 9px; letter-spacing: 2.4px; color: var(--gold);
    text-transform: uppercase; margin-bottom: 6px;
  }
  .where__address { font-style: normal; font-size: 20px; line-height: 27px; }

  /* Back */
  .appeal-frame {
    position: absolute; left: 106px; top: 183px;
    width: 317px; height: 280px; border: 1.5px solid var(--gold-line);
  }
  .appeal {
    position: absolute; left: 0; right: 0; top: 28px;
    text-align: center; font-size: 18.5px; line-height: 34px;
    padding: 0 22px;
  }
  .academy-name {
    position: absolute; left: 50%; top: 454px; transform: translateX(-50%);
    background: var(--hunter); padding: 0 10px;
    font-size: 15px; line-height: 18px; color: var(--ivory);
    white-space: nowrap;
  }
  .contact {
    position: absolute; left: 0; right: 0; top: 611px;
    text-align: center; list-style: none;
    font-family: "Josefin Sans", Arial, sans-serif;
    font-size: 10px; letter-spacing: 2.2px; color: var(--gold);
    text-transform: uppercase;
  }
  .contact li { line-height: 12px; margin-bottom: 13px; }
  .contact li:last-child { margin-bottom: 0; }
  .gold-band {
    position: absolute; left: 0; bottom: 0; width: 100%; height: 9px;
    background: var(--gold);
  }
</style>
</head>
<body>
<main class="canvas">
  <section class="card card--front" aria-label="Save the date, front">
    <div class="watermark" aria-hidden="true">Save<br>The<br>Date</div>
    <div class="title-rule"></div>
    <h1 class="title">Annual<br>Fund Leadership<br>Dinner</h1>
    <p class="when">June<br>20<br>2023<span class="when__time">6:30 pm</span></p>
    <div class="divider"></div>
    <div class="where">
      <p class="where__label">Location:</p>
      <address class="where__address">The Pellimore's Home<br>4187 Brindlecove Ridge Rd<br>Harrison, TN 37598</address>
    </div>
  </section>

  <section class="card card--back" aria-label="Save the date, back">
    <div class="appeal-frame">
      <p class="appeal">We would prayerfully ask that you consider partnering with us as we kick off our Annual Fund this Fall to celebrate our 25 year anniversary as an Academy.</p>
    </div>
    <p class="academy-name">Corvellan Prep</p>
    <ul class="contact">
      <li>www.corvellanprep.org</li>
      <li>423-555-0184</li>
      <li>advancement@corvellanprep.org</li>
    </ul>
    <div class="gold-band"></div>
  </section>
</main>
</body>
</html>
```